Ember & Rise Product Formulation & Benefits

Ember and Rise's formulation represents a complex formulation of essential all natural ingredients that reduce stress & anxiety, improve mood, with an elevated mood and euphoric sense of well-being, deliver three stage energy boosters, grass fed bovine collagen and vitamins B6 and B12.
based upon the complexity and the range of physical and mental health benefits we are seeking an animated infographic that will educate consumers on the ingredients and their benefits.

Target Market(s)

Coffee, Hemp and Funcational Beverage Consumers

Industry/Entity Type

Functional Food & Beverage

Requirements
Must have
• cross reference of ingredients to their benefits (see website)
Nice to have
• a concept of a puzzle that comes together, each piece with info on it, that when complete illustrates an image of a healthy lifestyle, coffees beverages, with company logo.

```html
<!DOCTYPE html>
<html lang="en">
<head>
<meta charset="utf-8">
<title>Ember &amp; Rise — Ingredients &amp; Benefits</title>
<link rel="stylesheet" href="https://fonts.googleapis.com/css2?family=Anton&family=Poppins:ital,wght@0,400;0,500;1,400&display=swap">
<style>
  :root {
    --mint: #0dfcaa;
    --navy: #1b2d38;
    --white: #f4f7f6;
    --latte: #d6a866;
    --cream: #ece6da;
  }
  * { margin: 0; padding: 0; box-sizing: border-box; }
  html, body { width: 1200px; height: 1200px; overflow: hidden; background: var(--navy); }
  .infographic {
    position: relative;
    width: 1200px;
    height: 1200px;
    background: var(--navy);
    font-family: "Poppins", sans-serif;
    color: var(--white);
    overflow: hidden;
  }
  .backdrop { position: absolute; inset: 0; }
  .title {
    position: absolute;
    top: 62px; left: 0; width: 1200px;
    text-align: center;
    font-family: "Anton", sans-serif;
    font-size: 76px;
    line-height: 1;
    letter-spacing: 0.5px;
    color: var(--navy);
  }
  .product-visual {
    position: absolute;
    left: 444px; top: 356px;
    width: 312px; height: 280px;
    border-radius: 50%;
    background: radial-gradient(ellipse at 50% 42%, var(--latte) 0%, #c99a5e 38%, var(--cream) 66%, rgba(27,45,56,0) 71%);
  }
  .label {
    position: absolute;
    font-family: "Anton", sans-serif;
    font-size: 23px;
    line-height: 1.4;
    color: var(--mint);
    white-space: nowrap;
  }
  .label--right { text-align: right; }
  .ingredient-list {
    position: absolute;
    list-style: none;
    font-style: italic;
    font-size: 17px;
    line-height: 21.5px;
    color: var(--white);
    white-space: nowrap;
  }
  .benefits-heading {
    position: absolute;
    top: 898px; left: 0; width: 1200px;
    text-align: center;
    font-family: "Anton", sans-serif;
    font-size: 52px;
    line-height: 1;
  }
  .benefits-heading .accent { color: var(--mint); }
  .benefits-heading .plain { color: var(--white); }
  .rule {
    position: absolute;
    top: 929px;
    height: 3px;
    background: var(--mint);
  }
  .brand {
    position: absolute;
    left: 44px; top: 1000px;
    display: flex; align-items: center; gap: 18px;
  }
  .brand-dot {
    width: 116px; height: 116px;
    border: 2px solid var(--white);
    border-radius: 50%;
  }
  .brand-name {
    font-family: "Anton", sans-serif;
    font-size: 54px;
    line-height: 1.02;
    color: var(--mint);
  }
  .divider {
    position: absolute;
    left: 429px; top: 992px;
    width: 3px; height: 148px;
    background: var(--mint);
  }
  .benefit-list {
    position: absolute;
    list-style: none;
    font-size: 21px;
    line-height: 28px;
    color: var(--white);
  }
  .benefit-list li { position: relative; padding-left: 22px; }
  .benefit-list li::before {
    content: "";
    position: absolute; left: 0; top: 10px;
    width: 13px; height: 10px;
    border-radius: 50%;
    background: var(--white);
    transform: rotate(-30deg);
  }
</style>
</head>
<body>
<main class="infographic">
  <svg class="backdrop" width="1200" height="1200" viewBox="0 0 1200 1200" aria-hidden="true">
    <defs>
      <radialGradient id="ring-glow" cx="50%" cy="50%" r="50%">
        <stop offset="70%" stop-color="rgba(13,252,170,0)"/>
        <stop offset="88%" stop-color="rgba(13,252,170,0.14)"/>
        <stop offset="100%" stop-color="rgba(13,252,170,0)"/>
      </radialGradient>
    </defs>
    <circle cx="600" cy="487" r="340" fill="url(#ring-glow)"/>
    <path d="M0,0 H1200 V205 Q1000,262 796,260 A300,300 0 0 0 404,260 Q200,262 0,205 Z" fill="var(--mint)"/>
    <circle cx="600" cy="487" r="288" fill="none" stroke="var(--mint)" stroke-width="3" stroke-dasharray="10 8"/>

    <g class="icon icon--outline">
      <circle cx="366" cy="324" r="38" fill="var(--navy)" stroke="var(--mint)" stroke-width="3"/>
      <path d="M366,302 L372,322 L388,314 L376,330 L366,334 L356,330 L344,314 L360,322 Z M366,334 V346" fill="var(--mint)" stroke="var(--mint)" stroke-width="2"/>
    </g>
    <g class="icon icon--outline">
      <circle cx="838" cy="324" r="38" fill="var(--navy)" stroke="var(--mint)" stroke-width="3"/>
      <polygon points="838,305 855,314.5 855,333.5 838,343 821,333.5 821,314.5" fill="none" stroke="var(--mint)" stroke-width="3"/>
      <g fill="var(--mint)">
        <circle cx="838" cy="305" r="3.5"/><circle cx="855" cy="314.5" r="3.5"/><circle cx="855" cy="333.5" r="3.5"/>
        <circle cx="838" cy="343" r="3.5"/><circle cx="821" cy="333.5" r="3.5"/><circle cx="821" cy="314.5" r="3.5"/>
      </g>
    </g>
    <g class="icon icon--filled">
      <circle cx="320" cy="520" r="39" fill="var(--mint)"/>
      <ellipse cx="320" cy="520" rx="24" ry="20" fill="none" stroke="var(--navy)" stroke-width="3"/>
      <line x1="320" y1="500" x2="320" y2="540" stroke="var(--navy)" stroke-width="3"/>
    </g>
    <g class="icon icon--filled">
      <circle cx="887" cy="520" r="39" fill="var(--mint)"/>
      <path d="M862,535 L874,505 L880,535 L892,505 L898,535 L910,505" fill="none" stroke="var(--navy)" stroke-width="4" stroke-linejoin="round"/>
    </g>
    <g class="icon icon--outline">
      <circle cx="414" cy="699" r="38" fill="var(--navy)" stroke="var(--mint)" stroke-width="3"/>
      <path d="M392,698 H436 Q434,716 414,718 Q394,716 392,698 Z" fill="none" stroke="var(--mint)" stroke-width="3"/>
      <line x1="404" y1="724" x2="424" y2="724" stroke="var(--mint)" stroke-width="3"/>
      <path d="M404,696 Q402,684 410,680 Q414,690 414,696 M418,696 Q420,684 428,682 Q428,690 424,696" fill="none" stroke="var(--mint)" stroke-width="3"/>
    </g>
    <g class="icon icon--outline">
      <circle cx="792" cy="699" r="38" fill="var(--navy)" stroke="var(--mint)" stroke-width="3"/>
      <polygon points="800,672 778,704 792,704 784,728 806,694 792,694" fill="var(--mint)"/>
    </g>
    <g class="icon icon--filled">
      <circle cx="604" cy="770" r="39" fill="var(--mint)"/>
      <polygon points="604,752 618,760 618,776 604,784 590,776 590,760" fill="none" stroke="var(--navy)" stroke-width="3"/>
      <circle cx="604" cy="768" r="4" fill="var(--navy)"/>
    </g>
  </svg>

  <h1 class="title">OUR ALL-NATURAL INGREDIENTS</h1>

  <div class="product-visual" role="img" aria-label="Photo of a creamy café mocha in a stemmed glass on a saucer with coffee beans, a spoon and a product box"></div>

  <div class="label label--right" style="right:896px; top:308px;">HEMP DERIVED DELTA-9 THC</div>
  <div class="label" style="left:897px; top:308px;">VITAMINS B6 AND B12</div>

  <div class="label" style="left:61px; top:496px;">NOOTROPICS</div>
  <ul class="ingredient-list" style="left:66px; top:538px;">
    <li>-Organic Arabic Coffee</li>
    <li>-Coffee Berry Extract</li>
    <li>-L-Theanine</li>
  </ul>

  <div class="label" style="left:944px; top:488px;">GRASS FED BOVINE<br>COLLAGEN PROTEINS</div>

  <div class="label" style="left:152px; top:718px;">ADAPTOGENS</div>
  <ul class="ingredient-list" style="left:158px; top:753px;">
    <li>-Ashwagandha</li>
    <li>-Rhodiola</li>
    <li>-Bacopa Monnier</li>
  </ul>

  <div class="label" style="left:580px; top:826px;">CBD</div>

  <div class="label" style="left:858px; top:722px;">ENERGY BOOSTERS</div>
  <ul class="ingredient-list" style="left:864px; top:765px;">
    <li>-Natural Caffeine</li>
    <li>-MCT Oil (Powder)</li>
    <li>-Ancient Peat &amp; Apple Extract</li>
  </ul>

  <div class="rule" style="left:0; width:352px;"></div>
  <h2 class="benefits-heading"><span class="accent">FORMULATION</span> <span class="plain">BENEFITS</span></h2>
  <div class="rule" style="left:842px; width:358px;"></div>

  <div class="brand">
    <span class="brand-dot"></span>
    <span class="brand-name">EMBER &amp;<br>RISE</span>
  </div>

  <div class="divider"></div>

  <ul class="benefit-list" style="left:458px; top:1001px; width:350px;">
    <li style="margin-bottom:11px;">Experience increased focus</li>
    <li style="margin-bottom:10px;">Improved Focus</li>
    <li>Reducing stress and anxiety with Ember &amp; Rise</li>
  </ul>

  <ul class="benefit-list" style="left:821px; top:996px; width:340px;">
    <li style="margin-bottom:9px;">Increased and Sustained energy &amp; Elevated mood</li>
    <li style="margin-bottom:12px;">Euphoric Sense of Well-being</li>
    <li>Deep Restorative Sleep</li>
  </ul>
</main>
</body>
</html>
```